Birch and Bough Tree Services Business Card Design

We need a business card design for our company based in Melbourne, Australia. We are a tree services business. We already have a logo designed by a designer on craft hive, so obviously we would like this to be incorporated in to the design, including similar colours. The final design should be sleek.

It should have:

Marcus Whitfield
Chief Executive Officer

www.quillhollowarbor.com.au
marcus.whitfield@quillhollowarbor.com.au
0491 736 208

Industry/Entity Type

Business

```html
<!DOCTYPE html>
<html lang="en">
<head>
<meta charset="utf-8">
<title>Birch and Bough Tree Services – Business Card</title>
<link href="https://fonts.googleapis.com/css2?family=Open+Sans:wght@400;600&display=swap" rel="stylesheet">
<style>
  :root {
    --backdrop: #262626;
    --card-white: #ffffff;
    --leaf-green: #8ffc00;
    --ink: #141414;
    --muted: #6b6b6b;
  }
  * { margin: 0; padding: 0; box-sizing: border-box; }
  html, body {
    width: 1200px; height: 1077px; overflow: hidden;
    background: var(--backdrop);
  }
  .card-pair {
    position: absolute; top: 377px; left: 45px;
    display: flex; gap: 30px;
  }
  .card {
    position: relative; width: 540px; height: 322px; overflow: hidden;
  }
  .card-front { background: var(--card-white); }
  .card-back { background: var(--leaf-green); }

  .edge-stripes { position: absolute; left: 0; bottom: 0; width: 540px; height: 40px; }

  .brand { position: absolute; display: flex; flex-direction: column; align-items: center; }
  .brand-mark { border-radius: 50%; }
  .brand-name {
    font-family: "Open Sans", Arial, sans-serif;
    font-weight: 400; color: var(--ink); white-space: nowrap; line-height: 1.2;
  }
  .card-front .brand { left: 26px; top: 60px; width: 230px; }
  .card-front .brand-mark { width: 110px; height: 110px; background: var(--leaf-green); margin-bottom: 26px; }
  .card-front .brand-name { font-size: 14px; }

  .card-back .brand { left: 0; right: 0; top: 64px; }
  .card-back .brand-mark { width: 150px; height: 150px; background: var(--ink); margin-bottom: 30px; }
  .card-back .brand-name { font-size: 22px; }

  .details {
    position: absolute; left: 282px; top: 44px; width: 245px;
    font-family: "Open Sans", Arial, sans-serif; color: var(--ink);
  }
  .person-name { font-size: 24px; font-weight: 400; line-height: 1.2; }
  .person-role { font-size: 11px; color: var(--muted); margin-top: 4px; }
  .address { font-size: 11px; line-height: 1.45; margin-top: 30px; }
  .contact-list { list-style: none; margin-top: 48px; }
  .contact-list li {
    display: flex; align-items: center; gap: 7px;
    font-size: 10.5px; line-height: 1; margin-bottom: 8px; white-space: nowrap;
  }
  .contact-list svg { width: 11px; height: 11px; flex: none; fill: var(--ink); }
</style>
</head>
<body>
  <main class="card-pair">
    <section class="card card-front">
      <div class="brand">
        <div class="brand-mark"></div>
        <p class="brand-name">Birch and Bough Tree Services</p>
      </div>

      <div class="details">
        <h1 class="person-name">Marcus Whitfield</h1>
        <p class="person-role">Chief Executive Officer</p>
        <p class="address">18 Elm Lane<br>Melbourne VIC 3000</p>
        <ul class="contact-list">
          <li>
            <svg viewBox="0 0 12 12"><path d="M3 0h6a1 1 0 0 1 1 1v10a1 1 0 0 1-1 1H3a1 1 0 0 1-1-1V1a1 1 0 0 1 1-1zm0 1.5v8h6v-8z"/></svg>
            0491 736 208
          </li>
          <li>
            <svg viewBox="0 0 12 12"><path d="M2.5 1 4.5 1 5.5 3.8 4.2 5a7 7 0 0 0 2.8 2.8L8.2 6.5 11 7.5v2a1.5 1.5 0 0 1-1.5 1.5A8.5 8.5 0 0 1 1 2.5 1.5 1.5 0 0 1 2.5 1z"/></svg>
            03 9012 4471
          </li>
          <li>
            <svg viewBox="0 0 12 12"><path d="M0 2h12v8H0zm1 1v.4l5 3.2 5-3.2V3zm0 1.6V9h10V4.6L6 7.8z"/></svg>
            marcus.whitfield@quillhollowarbor.com.au
          </li>
          <li>
            <svg viewBox="0 0 12 12"><circle cx="6" cy="6" r="6"/></svg>
            www.quillhollowarbor.com.au
          </li>
        </ul>
      </div>

      <svg class="edge-stripes" viewBox="0 0 540 40" preserveAspectRatio="none">
        <polygon points="0,14 540,34 540,40 0,40" fill="var(--leaf-green)"/>
        <polygon points="0,24 150,32 0,40" fill="var(--ink)"/>
      </svg>
    </section>

    <section class="card card-back">
      <div class="brand">
        <div class="brand-mark"></div>
        <p class="brand-name">Birch and Bough Tree Services</p>
      </div>
    </section>
  </main>
</body>
</html>
```